Professional website for psychological services

Create a professional, easy to navigate website using soothing coastal images and incorporate company logo in design. Website is for a small private clinic that provides psychological services and must be appealing to professional men and women. A website I really like is www.velmorlodge.example I would love something like similar.

Target Market(s)

Professional men and women seeking psychological services

Industry/Entity Type

Mental Health

Number of Pages Required

5+ page

Requirements
Must have
• The website must incorporate the logo provided. The name of the company/website is Brindle Oak Wellness Aftercare. Colors must compliment the logo, must be coastal and soothing yet very professional. I would like a website like www.velmorlodge.example
• Pages will be:Home, Services, FAQ and Contact Us. The images included of the building and office are for the contact us page. Under the tab Servies: Individual Psychotherapy, Family Therapy, EMDR I will provide specific content for each.
Nice to have
• I want the website to be easy to navigate and the font easy to read. The writing on the logo is very light and I'm open to changing it slightly if it will be better aesthetically.
Should not have
• Please no pictures of any swimsuits, alcoholic beverages, etc. This is a professional psychological clinic.

```html
<!DOCTYPE html>
<html lang="en">
<head>
<meta charset="utf-8">
<title>Brindle Oak Wellness Aftercare</title>
<link rel="stylesheet" href="https://fonts.googleapis.com/css2?family=Bodoni+Moda:wght@400&family=Questrial&display=swap">
<style>
  :root {
    --ink: #1d1d22;
    --muted: #3a3a40;
    --teal: #2ea6bf;
    --sand: #e7d5bc;
    --sand-soft: rgba(234, 216, 190, 0.9);
    --brush: #e9d3b6;
    --paper: #ffffff;
    --pin: #3f3f4c;
  }
  * { margin: 0; padding: 0; box-sizing: border-box; }
  html, body { width: 1200px; height: 2239px; overflow: hidden; background: var(--paper); }
  body { position: relative; font-family: "Questrial", sans-serif; color: var(--ink); }
  .serif { font-family: "Bodoni Moda", serif; font-weight: 400; }
  .caps { text-transform: uppercase; letter-spacing: 0.22em; font-size: 15px; }

  /* Header */
  .brand { position: absolute; top: 56px; left: 0; width: 1200px; text-align: center; }
  .brand-dot { width: 22px; height: 22px; border-radius: 50%; background: var(--teal); margin: 0 auto 10px; }
  .brand-name { font-family: "Bodoni Moda", serif; font-size: 38px; color: var(--teal); letter-spacing: 0.02em; }
  .nav { position: absolute; top: 220px; left: 0; width: 1200px; display: flex; justify-content: center; gap: 10px; }
  .nav a { color: var(--ink); text-decoration: none; padding: 6px 14px; margin: 0 18px; }
  .nav a.is-active { background: var(--brush); border-radius: 14px 6px 12px 8px; }

  /* Hero */
  .hero { position: absolute; top: 297px; left: 0; width: 1200px; height: 531px; }
  .hero-photo { position: absolute; inset: 0;
    background: linear-gradient(180deg, #8fc0df 0%, #b9d6e4 22%, #7e9fb0 30%, #d7c1a3 48%, #ead8c0 75%, #e2c6a6 100%); }
  .hero-cliff { position: absolute; right: 0; top: 0; width: 280px; height: 270px;
    background: linear-gradient(160deg, #9a6d4b, #c59c76); opacity: 0.75; }
  .hero-card { position: absolute; left: 66px; top: 128px; width: 614px; height: 276px; background: var(--sand-soft); }
  .hero-title { position: absolute; left: 65px; top: 45px; font-size: 46px; line-height: 46px; letter-spacing: 0.03em; }
  .hero-links { position: absolute; left: 62px; top: 201px; display: flex; gap: 66px; }
  .link-underline { color: var(--ink); text-decoration: none; padding-bottom: 8px; border-bottom: 1.5px solid var(--ink); }

  /* Intro */
  .intro { position: absolute; top: 912px; left: 0; width: 1200px; text-align: center; }
  .intro-title { font-size: 50px; letter-spacing: 0.04em; }
  .intro-copy { width: 740px; margin: 40px auto 0; line-height: 30px; font-size: 15px; letter-spacing: 0.2em; text-transform: uppercase; color: var(--muted); }

  /* Location band */
  .location { position: absolute; top: 1243px; left: 0; width: 1200px; height: 157px; background: var(--sand); }
  .location-pin { position: absolute; left: 352px; top: 36px; }
  .location-address { position: absolute; left: 537px; top: 38px; line-height: 31px; }
  .location-address strong { font-weight: 400; letter-spacing: 0.28em; color: var(--ink); }
  .location-contact { position: absolute; left: 778px; top: 66px; }

  /* Team */
  .team { position: absolute; top: 1400px; left: 0; width: 1200px; height: 622px; }
  .team-photo { position: absolute; inset: 0;
    background: linear-gradient(180deg, #eef0ee 0%, #e3e6df 40%, #dfe6da 70%, #eadfdf 85%, #e6e6e8 100%); }
  .team-title { position: absolute; top: 88px; left: 0; width: 1200px; text-align: center; font-size: 46px; letter-spacing: 0.04em; }
  .team-title span { background: var(--brush); padding: 0 24px; border-radius: 10px 18px 8px 16px; }
  .member { position: absolute; top: 215px; width: 300px; text-align: center; }
  .member-portrait { width: 176px; height: 176px; border-radius: 50%; margin: 0 auto;
    background: radial-gradient(circle at 50% 55%, #8f6f5c 0%, #5d4a3e 45%, #3f6b35 80%); }
  .member-name { margin-top: 28px; }
  .member-email { margin-top: 18px; }
  .team-more { position: absolute; top: 528px; left: 518px; letter-spacing: 0.26em; }

  /* Footer */
  .footer { position: absolute; top: 2078px; left: 0; width: 1200px; font-size: 14px; letter-spacing: 0.22em; color: var(--muted); }
  .footer-email { position: absolute; left: 339px; font-variant: small-caps; }
  .footer-year { position: absolute; left: 803px; }
</style>
</head>
<body>
  <header>
    <div class="brand">
      <div class="brand-dot"></div>
      <div class="brand-name">Brindle Oak</div>
    </div>
    <nav class="nav caps">
      <a class="is-active" href="#">Home</a>
      <a href="#">Services</a>
      <a href="#">FAQ</a>
      <a href="#">Contact Us</a>
    </nav>
  </header>

  <section class="hero">
    <div class="hero-photo" role="img" aria-label="Sunny sandy beach with waves and sandstone cliffs">
      <div class="hero-cliff"></div>
    </div>
    <div class="hero-card">
      <h1 class="hero-title serif">Brindle Oak Wellness<br>Aftercare</h1>
      <div class="hero-links caps">
        <a class="link-underline" href="#">Our Services</a>
        <a class="link-underline" href="#">Our Team</a>
      </div>
    </div>
  </section>

  <section class="intro">
    <h2 class="intro-title serif">This is what we do.</h2>
    <p class="intro-copy">Lorem ipsum dolor sit amet, consectetur adipisicing elit, sed do eiusmod tempor incididunt ut labore et dolore magna aliqua. Ut enim ad minim veniam, quis nostrud exercitation ullamco laboris nisi ut aliquip ex ea commodo consequat.</p>
  </section>

  <section class="location">
    <svg class="location-pin" width="54" height="88" viewBox="0 0 54 88" aria-hidden="true">
      <path d="M27 2 C12 2 3 13 3 26 C3 42 27 68 27 68 C27 68 51 42 51 26 C51 13 42 2 27 2 Z" fill="var(--pin)"/>
      <circle cx="27" cy="25" r="8" fill="var(--sand)"/>
      <ellipse cx="27" cy="76" rx="24" ry="8" fill="none" stroke="var(--pin)" stroke-width="4"/>
    </svg>
    <div class="location-address caps">
      <strong>Address</strong><br>123 45 City<br>21 The Road
    </div>
    <a class="location-contact link-underline caps" href="#">Contact Us</a>
  </section>

  <section class="team">
    <div class="team-photo" role="img" aria-label="Faded view of the clinic building with palm trees"></div>
    <h2 class="team-title serif"><span>Our team.</span></h2>
    <div class="member caps" style="left:146px">
      <div class="member-portrait" role="img" aria-label="Portrait of a team member"></div>
      <p class="member-name">Persons Name</p>
      <p class="member-email">name@email.com</p>
    </div>
    <div class="member caps" style="left:454px">
      <div class="member-portrait" role="img" aria-label="Portrait of a team member"></div>
      <p class="member-name">Persons Name</p>
      <p class="member-email">name@email.com</p>
    </div>
    <div class="member caps" style="left:756px">
      <div class="member-portrait" role="img" aria-label="Portrait of a team member"></div>
      <p class="member-name">Persons Name</p>
      <p class="member-email">name@email.com</p>
    </div>
    <a class="team-more link-underline caps" href="#">Read About Us</a>
  </section>

  <footer class="footer">
    <span class="footer-email">Info@BrindleOakAftercare.example</span>
    <span class="footer-year">©2019</span>
  </footer>
</body>
</html>
```